Business Card Design

I would like a new business card design for an accounting firm that specializes in resolving clients tax problems. I want the card to give the impression that we are not your typical stodgy accounting firm, but at the same time we will get the job done.
Industry/Entity Type
Business
Contact Information for Business Card
Dorian T Welsby
Certified Public Accountant
38-27 52nd Street
Sunnyside, NY 11287
Tel: (718) 555-0142
Fax: (888) 555-0199
e-mail: dtwthecpa@ledgerpost.com
website: harborfilingreliefexperts.com

```html
<!DOCTYPE html>
<html lang="en">
<head>
<meta charset="utf-8">
<title>Dorian T Welsby – Business Card</title>
<link rel="stylesheet" href="https://fonts.googleapis.com/css2?family=Montserrat:wght@600&family=Open+Sans:wght@400&display=swap">
<style>
  :root {
    --slate-dark: #323843;
    --slate-light: #3e4450;
    --sky: #3fa9d4;
    --sky-deep: #1f8fc0;
    --sky-shade: #2a7fae;
    --white: #ffffff;
  }
  * { margin: 0; padding: 0; box-sizing: border-box; }
  html, body { width: 1200px; height: 703px; overflow: hidden; background: #ffffff; }
  .card {
    position: relative;
    width: 1200px;
    height: 703px;
    overflow: hidden;
    background: var(--sky);
    font-family: "Open Sans", Arial, sans-serif;
    color: var(--white);
  }
  .card__band {
    position: absolute;
    left: 0; top: 0;
    width: 1200px;
    height: 703px;
  }
  .card__texture {
    position: absolute;
    left: 560px; top: 266px;
    width: 640px; height: 437px;
    background:
      radial-gradient(ellipse at 75% 65%, rgba(31,143,192,0.75) 0%, rgba(31,143,192,0.35) 45%, rgba(63,169,212,0) 75%),
      linear-gradient(160deg, rgba(63,169,212,0) 0%, rgba(42,127,174,0.35) 100%);
  }
  .identity {
    position: absolute;
    left: 134px;
    top: 92px;
  }
  .identity__name {
    font-family: "Montserrat", Arial, sans-serif;
    font-weight: 600;
    font-size: 48px;
    line-height: 1;
    letter-spacing: -1px;
  }
  .identity__title {
    margin-top: 14px;
    font-size: 27px;
    line-height: 1;
  }
  .contacts {
    position: absolute;
    left: 178px;
    top: 370px;
    list-style: none;
  }
  .contacts__item {
    display: flex;
    align-items: center;
    height: 48px;
    margin-bottom: 17px;
    font-size: 27.5px;
  }
  .contacts__item:first-child { margin-bottom: 22px; }
  .contacts__icon {
    width: 52px;
    height: 48px;
    margin-right: 27px;
    flex: none;
  }
  .contacts__fax { margin-left: 36px; }
</style>
</head>
<body>
<div class="card">
  <svg class="card__band" viewBox="0 0 1200 703" aria-hidden="true">
    <defs>
      <linearGradient id="slate" x1="0" y1="0" x2="1" y2="0">
        <stop offset="0" stop-color="#323843"/>
        <stop offset="1" stop-color="#3e4450"/>
      </linearGradient>
    </defs>
    <path d="M0 0 H1200 V266 H250 L202 325 L137 203 L99 266 H0 Z" fill="url(#slate)"/>
  </svg>

  <div class="card__texture" role="img" aria-label="Soft pattern of overlapping translucent blue diamonds"></div>

  <header class="identity">
    <h1 class="identity__name">Dorian T Welsby</h1>
    <p class="identity__title">Certified Public Accountant</p>
  </header>

  <ul class="contacts">
    <li class="contacts__item">
      <svg class="contacts__icon" viewBox="0 0 52 48" aria-hidden="true">
        <path d="M26 3 L50 24 H43 V46 H31 V32 H21 V46 H9 V24 H2 Z" fill="#ffffff"/>
        <rect x="37" y="6" width="6" height="12" fill="#ffffff"/>
      </svg>
      <span>38-27 52nd Street Sunnyside, NY 11287</span>
    </li>
    <li class="contacts__item">
      <svg class="contacts__icon" viewBox="0 0 52 48" aria-hidden="true">
        <path d="M8 6 C12 2 16 4 18 8 L21 14 C22 17 20 19 18 21 C20 27 25 32 31 35 C33 33 35 31 38 32 L44 35 C48 37 49 41 46 44 C42 48 36 48 30 45 C18 39 11 31 6 20 C3 14 4 10 8 6 Z" fill="#ffffff"/>
      </svg>
      <span>(718) 555-0142</span>
      <span class="contacts__fax">Fax: (888) 555-0199</span>
    </li>
    <li class="contacts__item">
      <svg class="contacts__icon" viewBox="0 0 52 48" aria-hidden="true">
        <rect x="6" y="10" width="40" height="29" rx="2" fill="#ffffff"/>
        <path d="M7 12 L26 27 L45 12" fill="none" stroke="#3fa9d4" stroke-width="3"/>
      </svg>
      <span>dtwthecpa@ledgerpost.com</span>
    </li>
    <li class="contacts__item">
      <svg class="contacts__icon" viewBox="0 0 52 48" aria-hidden="true">
        <circle cx="26" cy="24" r="21" fill="#ffffff"/>
        <g fill="none" stroke="#3fa9d4" stroke-width="2.5">
          <ellipse cx="26" cy="24" rx="9" ry="21"/>
          <line x1="26" y1="3" x2="26" y2="45"/>
          <line x1="5" y1="24" x2="47" y2="24"/>
          <path d="M9 13 H43 M9 35 H43"/>
        </g>
      </svg>
      <span>harborfilingreliefexperts.com</span>
    </li>
  </ul>
</div>
</body>
</html>
```